Employment Agency Website Design

We are working with an employment agency in California.

Some sites to use for content/competitors and inspiration:

https://www.travinmoor.example/us/en
https://www.pelkoworksusa.example
https://www.dunmarhire.example
https://www.vantriga.example/en
https://www.ombrelusa.example
https://www.quilnstaffing.example

Thank you for taking the time to consider designing a website for us. We are web developers based in Stockton, CA, USA. Most of our projects go through the same process. Understanding this process may help you win a project with us. We custom-code all of our websites in-house. We don’t have any requirements as to what tools you use for your design, but we prefer Figma files. For any design that we label as four-stars, we send it to the client for review. The client picks the final design they want us to use. Once we complete this process, we will continue to show additional clients all the four-star sites and purchase them later. Your designs will have multiple chances to sell. For better chances of success, we ask that you follow these guidelines.

IMAGES:
If you use any images or icons in the design, we ask that you have a link to the asset so we can purchase the image/icon. Most of the designs we submit do not have the customer’s images on them unless they have some great images. Be creative; show us the feeling you are trying to portray with your image choices. Use any royalty-free site you choose. We subscribe to Adobe and mainly use their images, but we can purchase images outside of Adobe. PLEASE NOTE: we will not submit designs to clients with watermarks on the images.

FONTS:
We ask that you identify the fonts used in the design. This can be done in a message if you want. We typically use Google Fonts and Adobe Fonts.

CONTENT:
We're always open to different content and ideas. We often submit designs with stock images so the client can see our vision. We typically take pictures after the website launch to use their images with our vision. Lorem Ipsum is fine for paragraphs, but we ask that you write the headers in correct English. We want to be able to show the vision and identify the sections of the website.

INSPIRATION:
We typically add a couple of links in the brief of websites we like to help you get started in your design.

REVISIONS:
We do not often ask for revisions of the designs unless we see something in the design that may not appeal to the client. If there are slight changes that we want to make, we do that in the development process.

FEEDBACK:
We rarely give feedback on designs during the design process. We are working on many website projects and do not have the time to provide feedback. We usually respond if your request is well thought out and asks specific questions, but a note asking “feedback, please” usually goes unanswered.

```html
<!DOCTYPE html>
<html lang="en">
<head>
<meta charset="utf-8">
<title>Kestrel Talent – Employment Agency</title>
<link rel="stylesheet" href="https://fonts.googleapis.com/css2?family=Poppins:wght@300;400;500;600;700&family=Oswald:wght@600&display=swap">
<style>
:root{
  --red:#c8202f;
  --ink:#111111;
  --text:#3a3a3a;
  --muted:#6b6b6b;
  --soft:#f4f1f1;
  --field:#ececec;
  --white:#ffffff;
  --black:#0a0a0a;
  --pink:#f4d3d6;
}
*{box-sizing:border-box;margin:0;padding:0}
html,body{width:1200px;height:4515px;overflow:hidden}
body{position:relative;background:var(--white);font-family:'Poppins',sans-serif;color:var(--text)}
.abs{position:absolute}
.photo{position:absolute}
.btn{position:absolute;background:var(--red);color:var(--white);font:500 14px 'Poppins',sans-serif;display:flex;align-items:center;justify-content:center;text-transform:uppercase;letter-spacing:.2px}
.h2{position:absolute;font:600 38px/1.2 'Poppins',sans-serif;color:var(--ink)}
.rule{position:absolute;width:66px;height:2px;background:var(--ink)}
.para{position:absolute;font:300 13px/1.6 'Poppins',sans-serif;color:var(--text)}
.list{position:absolute;list-style:none}
.list li{position:relative;padding-left:38px;font:300 13px/1.75 'Poppins',sans-serif;color:var(--text)}
.list li svg{position:absolute;left:4px;top:6px}

/* header */
.brand{position:absolute;left:38px;top:26px;display:flex;align-items:center;gap:8px}
.brand-dot{width:30px;height:30px;border-radius:50%;background:var(--red)}
.brand-name{font:500 30px/1 'Poppins',sans-serif;color:var(--ink)}
.brand-tag{position:absolute;left:86px;top:66px;font:300 11px 'Poppins',sans-serif;color:var(--muted)}
.nav{position:absolute;top:42px;left:344px;display:flex;gap:27px;font:400 15px 'Poppins',sans-serif;color:var(--ink)}
.search-top{position:absolute;left:948px;top:30px;width:208px;height:44px;background:var(--white);border:1px solid #e2e2e2;font:300 12px 'Poppins',sans-serif;color:var(--muted);padding:13px 16px}
.search-top svg{position:absolute;right:14px;top:15px}

/* hero */
.hero-bg{left:0;top:0;width:1200px;height:713px;background:linear-gradient(90deg,#ffffff 0%,#f7f5f3 35%,#e4dcd4 62%,#cfc6bd 80%,#b8ab9e 100%)}
.hero-lead{position:absolute;left:128px;top:178px;font:600 36px/1.2 'Poppins',sans-serif;color:var(--ink)}
.hero-big{position:absolute;left:128px;top:230px;font:600 52px/1.1 'Oswald',sans-serif;color:var(--red);letter-spacing:.5px}
.hero-tail{position:absolute;left:130px;top:300px;font:600 36px/1.2 'Poppins',sans-serif;color:var(--ink)}
.hero-copy{left:133px;top:372px;width:440px;font-size:15px;line-height:1.7}

.finder{position:absolute;left:130px;top:659px;width:937px;height:119px;background:var(--white);box-shadow:0 10px 30px rgba(0,0,0,.08)}
.field{position:absolute;top:31px;height:56px;background:var(--field);font:300 12px 'Poppins',sans-serif;color:var(--text);display:flex;align-items:center;padding-left:52px}
.field svg{position:absolute;left:22px;top:19px}

/* about */
.hex{left:130px;top:815px;width:510px;height:594px}
.about-kicker{position:absolute;left:708px;top:855px;font:600 22px 'Poppins',sans-serif;color:var(--ink)}
.about-title{left:705px;top:886px;font-size:36px}

/* employers */
.band-soft{position:absolute;left:0;width:1200px;background:var(--soft)}

/* testimonials */
.card{position:absolute;top:3360px;height:342px;background:var(--white);padding:44px 42px 0}
.quote{font:700 44px/1 'Poppins',sans-serif;color:#d9d9d9;height:36px}
.card p{font:300 12.5px/1.6 'Poppins',sans-serif;color:var(--text);margin-top:4px}
.card .dash{width:34px;height:1px;background:#bbb;margin:28px 0 24px}
.card .who{font:300 12.5px 'Poppins',sans-serif;color:var(--text)}

/* footer */
.footer{position:absolute;left:0;top:4256px;width:1200px;height:259px;background:var(--black);color:var(--white)}
.foot-brand{position:absolute;left:134px;top:58px;display:flex;align-items:center;gap:10px}
.foot-brand .brand-dot{width:42px;height:42px;background:var(--white)}
.foot-brand .brand-name{color:var(--white);font-size:40px;font-weight:400}
.foot-tag{position:absolute;left:200px;top:112px;font:300 15px 'Poppins',sans-serif;color:#ddd}
.follow{position:absolute;left:834px;top:57px;font:300 14px 'Poppins',sans-serif;color:#ddd}
.socials{position:absolute;left:918px;top:48px;display:flex;gap:7px}
.socials span{width:32px;height:32px;border-radius:50%;background:var(--white);display:block}
.foot-nav{position:absolute;left:548px;top:115px;display:flex;gap:25px;font:300 14px 'Poppins',sans-serif;color:#ddd}
.foot-rule{position:absolute;left:134px;top:168px;width:934px;height:1px;background:#333}
.copy{position:absolute;left:0;width:1200px;top:200px;text-align:center;font:300 12px 'Poppins',sans-serif;color:#ccc}
</style>
</head>
<body>

<!-- Hero -->
<div class="photo hero-bg" role="img" aria-label="Two women reviewing work on a laptop at a café table with orange chairs"></div>

<header>
  <div class="brand"><span class="brand-dot"></span><span class="brand-name">kestreltalent</span></div>
  <div class="brand-tag">The future of work.</div>
  <nav class="nav"><span>Find Jobs</span><span>Hire Talent</span><span>Solutions</span><span>Insights</span><span>About us</span><span>Contact us</span></nav>
  <div class="search-top">Search Jobs
    <svg width="12" height="12" viewBox="0 0 12 12"><circle cx="5" cy="5" r="3.8" fill="none" stroke="#444" stroke-width="1.3"/><line x1="8" y1="8" x2="11" y2="11" stroke="#444" stroke-width="1.3"/></svg>
  </div>
</header>

<h1>
  <span class="hero-lead">Your Path to</span>
  <span class="hero-big">EMPLOYMENT EXCELLENCE</span>
  <span class="hero-tail">in California!</span>
</h1>
<p class="para hero-copy">Lorem ipsum dolor sit amet, consectetur adipiscing elit, sed do eiusmod tempor incididunt.</p>
<div class="btn" style="left:135px;top:449px;width:275px;height:54px">Explore the opportunities</div>

<div class="finder">
  <div class="field" style="left:35px;width:385px">
    <svg width="16" height="16" viewBox="0 0 16 16"><circle cx="6.5" cy="6.5" r="5" fill="none" stroke="#333" stroke-width="1.6"/><line x1="10.3" y1="10.3" x2="14.5" y2="14.5" stroke="#333" stroke-width="1.8"/></svg>
    Job Title, Skills, or Keywords</div>
  <div class="field" style="left:434px;width:291px;padding-left:46px">
    <svg width="14" height="18" viewBox="0 0 14 18"><path d="M7 1a6 6 0 0 0-6 6c0 4.5 6 10 6 10s6-5.5 6-10a6 6 0 0 0-6-6z" fill="#222"/><circle cx="7" cy="7" r="2.2" fill="#ececec"/></svg>
    City, State, or Zip Code</div>
  <div class="btn" style="left:739px;top:31px;width:168px;height:56px">Search</div>
</div>

<!-- About -->
<section>
  <svg class="abs" style="left:130px;top:815px" width="510" height="594" viewBox="0 0 510 594">
    <polygon points="255,0 510,150 510,450 255,594 0,450 0,150" fill="#f4d3d6"/>
    <polygon points="255,110 390,190 390,400 255,480 120,400 120,190" fill="#ffffff"/>
  </svg>
  <div class="photo" style="left:185px;top:835px;width:435px;height:574px;background:linear-gradient(180deg,rgba(200,185,215,.35),rgba(125,85,170,.85) 55%,rgba(95,60,140,.95))" role="img" aria-label="Smiling man in a purple jacket holding an open laptop"></div>
  <div class="about-kicker">About</div>
  <h2 class="h2 about-title">Kestrel Talent</h2>
  <div class="rule" style="left:706px;top:955px;width:108px"></div>
  <p class="para" style="left:708px;top:985px;width:380px">Sed ut perspiciatis unde omnis iste natus error sit volu ptatem accusantium doloremque laudantium, totam rem aperiam, eaque ipsa quae ab illo inventore veritatis et quasi architecto beatae vitae dicta sunt explicabo. Nemo enim ipsam voluptatem quia voluptas sit aspernatur aut odit aut fugit, sed quia consequuntur magni dolores eos qui ratione voluptatem sequi nesciunt</p>
  <ul class="list" style="left:700px;top:1161px">
    <li style="padding-left:30px;margin-bottom:5px"><svg width="8" height="12" viewBox="0 0 8 12"><path d="M1 1l5 5-5 5" fill="none" stroke="#222" stroke-width="1.4"/></svg>Lorem Ipsum is simply</li>
    <li style="padding-left:30px;margin-bottom:5px"><svg width="8" height="12" viewBox="0 0 8 12"><path d="M1 1l5 5-5 5" fill="none" stroke="#222" stroke-width="1.4"/></svg>Contrary to popular belief,</li>
    <li style="padding-left:30px"><svg width="8" height="12" viewBox="0 0 8 12"><path d="M1 1l5 5-5 5" fill="none" stroke="#222" stroke-width="1.4"/></svg>Nor again is there anyone who</li>
  </ul>
  <div class="btn" style="left:708px;top:1282px;width:142px;height:53px">Read more</div>
</section>

<!-- Employers -->
<section>
  <div class="band-soft" style="top:1409px;height:495px"></div>
  <div class="photo" style="left:525px;top:1409px;width:675px;height:495px;background:linear-gradient(90deg,#f4f1f1 0%,#e9e3df 25%,#d9cfc8 60%,#c9bcb3 100%)" role="img" aria-label="Cheerful woman holding a letter beside a laptop in a bright office"></div>
  <h2 class="h2" style="left:136px;top:1464px">Employers</h2>
  <div class="rule" style="left:138px;top:1539px"></div>
  <p class="para" style="left:137px;top:1581px;width:380px">Sed ut perspiciatis unde omnis iste natus error sit volu ptatem accusantium doloremque laudantium, totam rem aperiam, eaque ipsa quae ab illo inventore veritatis et quasi architecto beatae vitae dicta sunt explicabo. Nemo enim ipsam voluptatem quia voluptas sit aspernatur aut odit aut fugit, sed quia consequuntur magni dolores eos qui ratione voluptatem sequi nesciunt</p>
  <div class="btn" style="left:139px;top:1778px;width:142px;height:53px">Read more</div>
</section>

<!-- Find talent -->
<section>
  <svg class="abs" style="left:130px;top:1975px" width="422" height="490" viewBox="0 0 422 490" role="img" aria-label="Three colleagues discussing work around a laptop in a glass office">
    <defs><linearGradient id="g1" x1="0" y1="0" x2="1" y2="1"><stop offset="0" stop-color="#d8d6d3"/><stop offset=".6" stop-color="#9a928a"/><stop offset="1" stop-color="#6d655e"/></linearGradient></defs>
    <polygon points="0,0 370,0 422,490 0,490" fill="url(#g1)"/>
  </svg>
  <h2 class="h2" style="left:616px;top:1966px">Find talent to get<br>more done</h2>
  <div class="rule" style="left:618px;top:2091px"></div>
  <ul class="list" style="left:618px;top:2142px;width:450px">
    <li style="margin-bottom:21px"><svg width="10" height="18" viewBox="0 0 10 18"><path d="M1 1l7 8-7 8" fill="none" stroke="#222" stroke-width="1.5"/></svg>Sed ut perspiciatis unde omnis iste natus error sit volu ptatem accusantium doloremque laudantium, totam rem aperiam, eaque ipsa quae ab.</li>
    <li style="margin-bottom:21px"><svg width="10" height="18" viewBox="0 0 10 18"><path d="M1 1l7 8-7 8" fill="none" stroke="#222" stroke-width="1.5"/></svg>Contrary to popular belief, Lorem Ipsum is not simply random text. It has roots in a piece of classical .</li>
    <li><svg width="10" height="18" viewBox="0 0 10 18"><path d="M1 1l7 8-7 8" fill="none" stroke="#222" stroke-width="1.5"/></svg>It is a long established fact that a reader will be distracted by the readable content of a page when looking</li>
  </ul>
  <div class="btn" style="left:620px;top:2407px;width:216px;height:53px">Find your next hire</div>
</section>

<!-- Consulting -->
<section>
  <h2 class="h2" style="left:130px;top:2554px">Consulting solutions<br>to drive business<br>impact</h2>
  <div class="rule" style="left:132px;top:2729px"></div>
  <ul class="list" style="left:132px;top:2779px;width:460px">
    <li style="margin-bottom:21px"><svg width="10" height="18" viewBox="0 0 10 18"><path d="M1 1l7 8-7 8" fill="none" stroke="#222" stroke-width="1.5"/></svg>Sed ut perspiciatis unde omnis iste natus error sit volu ptatem accusantium doloremque laudantium, totam rem aperiam, eaque ipsa quae ab.</li>
    <li style="margin-bottom:21px"><svg width="10" height="18" viewBox="0 0 10 18"><path d="M1 1l7 8-7 8" fill="none" stroke="#222" stroke-width="1.5"/></svg>Contrary to popular belief, Lorem Ipsum is not simply random text. It has roots in a piece of classical .</li>
    <li><svg width="10" height="18" viewBox="0 0 10 18"><path d="M1 1l7 8-7 8" fill="none" stroke="#222" stroke-width="1.5"/></svg>It is a long established fact that a reader will be distracted by the readable content of a page when looking</li>
  </ul>
  <div class="btn" style="left:135px;top:3043px;width:142px;height:53px">Read more</div>
  <svg class="abs" style="left:650px;top:2570px" width="419" height="531" viewBox="0 0 419 531" role="img" aria-label="Three smiling coworkers gathered around a laptop">
    <defs><linearGradient id="g2" x1="0" y1="0" x2="0" y2="1"><stop offset="0" stop-color="#cfc9c2"/><stop offset=".5" stop-color="#8f857c"/><stop offset="1" stop-color="#5a524b"/></linearGradient></defs>
    <polygon points="30,0 419,0 419,531 0,531" fill="url(#g2)"/>
  </svg>
</section>

<!-- Testimonials -->
<section>
  <div class="band-soft" style="top:3168px;height:588px"></div>
  <h2 class="h2" style="left:0;top:3220px;width:1200px;text-align:center">Customer Testimonials</h2>
  <div class="rule" style="left:567px;top:3305px"></div>
  <svg class="abs" style="left:62px;top:3514px" width="18" height="36" viewBox="0 0 18 36"><path d="M16 2L3 18l13 16" fill="none" stroke="#888" stroke-width="1.8"/></svg>
  <svg class="abs" style="left:1110px;top:3514px" width="18" height="36" viewBox="0 0 18 36"><path d="M2 2l13 16L2 34" fill="none" stroke="#888" stroke-width="1.8"/></svg>

  <div class="card" style="left:131px;width:295px"><div class="quote">&ldquo;</div><p>Lorem ipsum dolor sit amet, cons ectetur adipiscing elit, sed do eius mod tempor incididunt ut labore et dolore magna aliqua. Ut enim ad minim ven iam, quis nos trud exercit ation ullamco laboris nisi ut aliquip ex ea commodo Duis aute irure dolor in repre.</p><div class="dash"></div><div class="who">Dana Hollis</div></div>
  <div class="card" style="left:455px;width:293px"><div class="quote">&ldquo;</div><p>Lorem ipsum dolor sit amet, cons ectetur adipiscing elit, sed do eius mod tempor incididunt ut labore et dolore magna aliqua. Ut enim ad minim ven iam, quis nos trud exercit ation ullamco laboris nisi ut aliquip ex ea commodo Duis aute irure dolor in repre.</p><div class="dash"></div><div class="who">Dana Hollis</div></div>
  <div class="card" style="left:773px;width:294px"><div class="quote">&ldquo;</div><p>Lorem ipsum dolor sit amet, cons ectetur adipiscing elit, sed do eius mod tempor incididunt ut labore et dolore magna aliqua. Ut enim ad minim ven iam, quis nos trud exercit ation ullamco laboris nisi ut aliquip ex ea commodo Duis aute irure dolor in repre.</p><div class="dash"></div><div class="who">Dana Hollis</div></div>
</section>

<!-- Workforce -->
<section>
  <div class="photo" style="left:0;top:3756px;width:1200px;height:500px;background:linear-gradient(90deg,#7b746e 0%,#a39b94 30%,#d9d5d1 52%,#ebe9e7 62%,#efeeed 100%)" role="img" aria-label="Overhead view of a team meeting around a long conference table"></div>
  <h2 class="h2" style="left:676px;top:3828px;line-height:1.4">Helping you solve<br>your workforce<br>challenges.</h2>
  <p class="para" style="left:677px;top:4012px;width:380px;font-size:14px">Sed ut perspiciatis unde omnis iste natus error sit volu ptatem accusantium doloremque laudantium, totam rem aperiam.</p>
  <div class="btn" style="left:678px;top:4110px;width:149px;height:53px">Contact us</div>
</section>

<!-- Footer -->
<footer class="footer">
  <div class="foot-brand"><span class="brand-dot"></span><span class="brand-name">kestreltalent</span></div>
  <div class="foot-tag">The future of work.</div>
  <div class="follow">Follow us</div>
  <div class="socials"><span></span><span></span><span></span><span></span></div>
  <nav class="foot-nav"><span>Find Jobs</span><span>Hire Talent</span><span>Solutions</span><span>Insights</span><span>About us</span><span>Contact us</span></nav>
  <div class="foot-rule"></div>
  <div class="copy">Copyright © 2024 All Rights Reserved</div>
</footer>

</body>
</html>
```